Wordpress Website for electrician

I'm looking for an easy to maintain website for my electrical contracting business. Need a professional and appealing site.
Im wanting a website where clients can come on and look at services we offer, case studies and advertise our services.
Colours I'm wanting to incorporate are green, white, black and grey
I'm wanting a big slide show on main page where I can place advertising etc.
Menu is to include home, services, our work, specials, energy efficiency and contact
My existing site is www.trelwirefix.com.au
Updates
looking for something with a similar layout to this website
Target Market(s)
Businesses
Industry/Entity Type
Electrician
Look and feel

```html
<!DOCTYPE html>
<html lang="en">
<head>
<meta charset="utf-8">
<title>Trelwire Fix – Electrical Contractor</title>
<link href="https://fonts.googleapis.com/css2?family=Source+Sans+3:wght@300;400;600;700;900&display=swap" rel="stylesheet">
<style>
:root{
  --green:#3db54a;
  --green-dark:#1f8a34;
  --green-soft:#7dcf90;
  --orange:#f6b642;
  --ink:#231f20;
  --text:#4a4a4a;
  --muted:#7a7a7a;
  --line:#dcdcdc;
  --grey-bg:#ececec;
  --band:#cfcfcf;
  --blue:#2e7ea0;
  --white:#fff;
}
*{box-sizing:border-box;margin:0;padding:0}
html,body{width:1029px;height:1200px;overflow:hidden}
body{position:relative;background:var(--white);font-family:"Source Sans 3",sans-serif;color:var(--text)}
.abs{position:absolute}
.topbar{left:0;top:0;width:1029px;height:21px;background:var(--ink);border-bottom:2px solid var(--green)}
.topbar .links{position:absolute;right:18px;top:4px;font-size:9.5px;color:#ddd}
.topbar .links span{margin:0 3px}
.brand{left:92px;top:50px;display:flex;align-items:center;gap:10px}
.brand .dot{width:22px;height:22px;border-radius:50%;background:var(--green)}
.brand .name{font-size:32px;font-weight:600;color:var(--green);letter-spacing:.5px}
.brand-sub{left:124px;top:88px;font-size:10px;color:var(--muted)}
.contact{left:690px;top:42px;width:205px}
.contact .lead{font-size:11.5px;color:var(--muted);border-bottom:1px solid var(--line);padding-bottom:3px}
.contact .row{display:flex;align-items:center;gap:6px;font-size:15px;color:var(--green);margin-top:5px}
.nav{left:0;top:123px;width:1029px;height:36px;background:#f4f4f4;border-top:1px solid #e2e2e2;border-bottom:1px solid #e2e2e2}
.nav a{position:absolute;top:11px;font-size:11.5px;color:#333;text-decoration:none}
.nav a.on{color:var(--green)}
.nav .sep{position:absolute;top:7px;width:1px;height:22px;background:#d6d6d6}
.search{left:761px;top:128px;width:144px;height:25px;border:1px solid #ddd;border-radius:13px;background:#fff}
.search span{position:absolute;left:16px;top:5px;font-size:11px;font-style:italic;color:#aaa}
.search .btn{position:absolute;right:-1px;top:-1px;width:33px;height:25px;border-radius:0 13px 13px 0;background:var(--green);display:flex;align-items:center;justify-content:center}
.hero-bg{left:0;top:159px;width:1029px;height:274px;background:var(--grey-bg)}
.banner{left:69px;top:169px;width:838px;height:243px;box-shadow:0 5px 6px rgba(0,0,0,.25)}
.tab{position:absolute;top:0;height:243px;background:linear-gradient(90deg,#2a9b3c,#3db54a);border-right:1px solid #2e8e3c;display:flex;align-items:flex-end;justify-content:center}
.tab span{writing-mode:vertical-rl;transform:rotate(180deg);color:#fff;font-size:18px;padding-bottom:14px;white-space:nowrap}
.slide{position:absolute;left:48px;top:0;width:601px;height:243px;background:#fff}
.product{position:absolute;left:60px;top:20px;width:210px;height:170px;background:linear-gradient(135deg,#8c55a8,#c9c3d6 60%,#e6e6e6);border-radius:6px}
.cond{position:absolute;left:74px;top:214px;font-size:14px;font-weight:700;color:var(--ink)}
.led-title{position:absolute;left:212px;top:12px;font-size:41px;font-weight:900;color:var(--green);letter-spacing:-.5px}
.led-sub{position:absolute;left:278px;top:54px;font-size:22px;font-weight:700;color:var(--ink)}
.price{position:absolute;left:280px;top:92px;font-size:90px;font-weight:900;color:var(--green-soft);line-height:1}
.each{position:absolute;left:466px;top:108px;font-size:20px;font-weight:700;color:var(--green-soft)}
.click{position:absolute;left:257px;top:208px;font-size:22px;font-weight:700;color:var(--orange)}
h2.sec{position:absolute;font-size:21px;font-weight:400;color:var(--green);text-transform:uppercase;letter-spacing:.2px}
p.copy{position:absolute;font-size:10.5px;line-height:19px;color:var(--text)}
.pill{position:absolute;height:22px;border-radius:11px;color:#fff;font-size:12.5px;font-weight:600;padding-left:16px;display:flex;align-items:center;border:1px solid rgba(0,0,0,.2)}
.pill.g{background:linear-gradient(#5cc865,#2f9b3d)}
.pill.b{background:linear-gradient(#4a9ac0,#236e90)}
.pill i{position:absolute;right:9px;top:5px;width:12px;height:12px;border-radius:50%;background:#fff}
.pill i:after{content:"";position:absolute;left:4.5px;top:3px;border-left:4px solid #333;border-top:3px solid transparent;border-bottom:3px solid transparent}
.green-box{left:356px;top:627px;width:195px;height:156px;background:#fff;box-shadow:0 1px 5px rgba(0,0,0,.25)}
.green-box .bulb{position:absolute;left:80px;top:8px;width:34px;height:48px;border-radius:50%;background:radial-gradient(#c8e6b8,#5a8a4a)}
.green-box .t1{position:absolute;left:0;width:100%;text-align:center;top:54px;font-size:33px;font-weight:900;color:var(--green)}
.green-box .t2{position:absolute;left:0;width:100%;text-align:center;top:86px;font-size:24px;font-weight:900;color:var(--ink)}
.green-box .grass{position:absolute;left:4px;right:4px;bottom:6px;height:14px;background:linear-gradient(#9bd77a,#3c8f2a)}
.svc{position:absolute;left:588px;width:311px;border:1px solid #e3e3e3;border-radius:7px;background:#fff;box-shadow:0 1px 3px rgba(0,0,0,.08)}
.svc h3{position:absolute;left:60px;font-size:20px;font-weight:400;color:var(--green)}
.svc p{position:absolute;left:60px;font-size:10.5px;line-height:17px;color:var(--text);width:240px}
.svc svg{position:absolute;left:14px}
.band{left:0;top:809px;width:1029px;height:147px;background:repeating-linear-gradient(45deg,#d2d2d2 0 2px,#c8c8c8 2px 4px)}
.case{position:absolute;top:829px;width:251px;height:105px;background:#fff}
.case .ph{position:absolute;left:10px;top:9px;width:81px;height:87px;background:linear-gradient(#6d5a4a,#e8e8e8 40%,#cfcfcf)}
.case h4{position:absolute;left:101px;top:6px;font-size:15px;font-weight:400;color:var(--green)}
.case p{position:absolute;left:101px;top:29px;width:145px;font-size:9.5px;line-height:15.5px;color:#333}
.case .more{position:absolute;right:12px;bottom:7px;font-size:12px;color:var(--green);display:flex;align-items:center;gap:6px}
.case .more b{display:inline-block;width:14px;height:14px;border-radius:50%;background:var(--green);position:relative}
.case .more b:after{content:"";position:absolute;left:5px;top:3.5px;border-left:5px solid #fff;border-top:3.5px solid transparent;border-bottom:3.5px solid transparent}
.foot-h{position:absolute;top:972px;font-size:21px;font-weight:400;color:var(--green)}
.vline{position:absolute;top:972px;width:1px;height:180px;background:#e2e2e2}
.news{position:absolute;left:92px;width:205px}
.news h5{font-size:10.5px;font-weight:600;color:#444;text-transform:uppercase}
.news p{font-size:9.5px;line-height:15px;color:#555;margin-top:2px}
.news p a,.green-link{color:var(--green);text-decoration:none}
.quote{left:333px;top:1010px;width:190px;font-size:9.5px;line-height:17px;color:#555}
.form-intro{left:570px;top:996px;width:260px;font-size:9.5px;line-height:13px;color:#555}
.field{position:absolute;left:570px;font-size:9.5px;color:#777}
.field span{position:absolute;left:51px;top:-6px;width:135px;height:21px;border:1px solid #ddd;background:#fff}
.badge{left:769px;top:1043px;width:86px;height:68px;background:linear-gradient(135deg,#2f7fc2,#f3d23a 50%,#3db54a)}
.badge-bar{left:732px;top:1126px;width:164px;height:16px;background:#e6e6e6;border-radius:2px}
.footer{left:0;top:1166px;width:1029px;height:34px;background:var(--ink);border-top:4px solid var(--green)}
.footer p{position:absolute;left:95px;top:9px;font-size:10px;color:#ddd}
</style>
</head>
<body>

<header>
  <div class="abs topbar"><div class="links">Cookies<span>|</span>Site map<span>|</span>Ts&amp;Cs</div></div>
  <div class="abs brand"><div class="dot"></div><div class="name">trelwirefix</div></div>
  <div class="abs brand-sub">electrical contractor</div>
  <div class="abs contact">
    <div class="lead">Contact us today for more details</div>
    <div class="row"><svg width="12" height="12" viewBox="0 0 12 12"><circle cx="6" cy="6" r="6" fill="#3db54a"/><path d="M3.8 3.2l1.2-.4.7 1.5-.7.6a4 4 0 0 0 1.9 1.9l.6-.7 1.5.7-.4 1.2c-2.7.2-5-2.1-4.8-4.8z" fill="#fff"/></svg>0400 555 019</div>
    <div class="row"><svg width="12" height="10" viewBox="0 0 12 10"><rect width="12" height="10" fill="#3db54a"/><path d="M0 0l6 5 6-5" stroke="#fff" fill="none"/></svg>info@trelwirefix.com.au</div>
  </div>
  <nav class="abs nav">
    <a class="on" style="left:92px">HOME</a><i class="sep" style="left:149px"></i>
    <a style="left:174px">SERVICES</a><i class="sep" style="left:245px"></i>
    <a style="left:267px">OUR WORK</a><i class="sep" style="left:345px"></i>
    <a style="left:369px">SPECIALS ENERGY</a><i class="sep" style="left:478px"></i>
    <a style="left:496px">EFFICIENCY</a><i class="sep" style="left:572px"></i>
    <a style="left:590px">CONTACT</a>
  </nav>
  <div class="abs search"><span>search</span><div class="btn"><svg width="15" height="15" viewBox="0 0 15 15"><circle cx="6" cy="6" r="4.5" stroke="#fff" stroke-width="1.6" fill="none"/><path d="M9.3 9.3l4.2 4.2" stroke="#fff" stroke-width="2"/></svg></div></div>
</header>

<section class="abs hero-bg"></section>
<section class="abs banner">
  <div class="tab" style="left:0;width:48px"><span>Special offers</span></div>
  <div class="slide">
    <div class="product" role="img" aria-label="Boxed LED downlight kit with fitting and bulb"></div>
    <div class="cond">CONDITIONS APPLY</div>
    <div class="led-title">LED DOWNLIGHTS</div>
    <div class="led-sub">Supplied &amp; Installed</div>
    <div class="price">$33</div>
    <div class="each">EACH</div>
    <div class="click">Click here for more details</div>
  </div>
  <div class="tab" style="left:649px;width:47px"><span>Electrical Contracting</span></div>
  <div class="tab" style="left:696px;width:47px"><span>Energy Efficiency</span></div>
  <div class="tab" style="left:743px;width:48px"><span>Underground Locating</span></div>
  <div class="tab" style="left:791px;width:47px"><span>Contact us</span></div>
</section>

<main>
  <h2 class="sec" style="left:88px;top:453px">LED is the future</h2>
  <p class="copy" style="left:88px;top:485px;width:460px">LED lighting has involved rapidly in the last 5 years. In the coming years we will see all lighting being substitued with LED lights. It is by far the most efficient form of lighting on todays market. Let us retrofit your business or home with LED and the savings will literally pay the lights off.</p>
  <div class="pill g" style="left:85px;top:553px;width:127px">Why LEDs?<i></i></div>
  <div class="pill b" style="left:226px;top:553px;width:153px">Request a quote<i></i></div>

  <h2 class="sec" style="left:84px;top:593px">Reduce your business energy consumption</h2>
  <p class="copy" style="left:84px;top:629px;width:262px">By letting us analyse your energy consumption, we can identify where you are simply burning your money. We can suggest and implement easy solutions to save you money and minimise your carbon emissions.</p>
  <div class="pill g" style="left:77px;top:722px;width:200px">ENERGY EFFICIENCY AUDIT?<i></i></div>
  <div class="pill b" style="left:78px;top:751px;width:144px">BOOK AUDIT NOW<i></i></div>
  <div class="abs green-box">
    <div class="bulb" role="img" aria-label="Light bulb with a small tree growing inside"></div>
    <div class="t1">BE GREEN</div>
    <div class="t2">SAVE MONEY</div>
    <div class="grass" role="img" aria-label="Strip of green grass"></div>
  </div>

  <h2 class="sec" style="left:585px;top:453px">Our services</h2>
  <div class="svc" style="top:485px;height:78px">
    <svg style="top:20px" width="28" height="42" viewBox="0 0 28 42"><circle cx="14" cy="13" r="13" fill="#7dcf90"/><rect x="8" y="24" width="12" height="10" fill="#7dcf90"/><rect x="10" y="36" width="8" height="4" rx="2" fill="#7dcf90"/></svg>
    <h3 style="top:10px">ELECTRICAL CONTRACTING</h3>
    <p style="top:36px">We offer all types of electrical work from Installation to maintenance</p>
  </div>
  <div class="svc" style="top:569px;height:94px">
    <svg style="top:32px" width="34" height="32" viewBox="0 0 34 32"><path d="M28 16a12 12 0 1 1-4-9" stroke="#7dcf90" stroke-width="6" fill="none"/><path d="M18 2h12v12z" fill="#7dcf90"/></svg>
    <h3 style="top:6px">ENERGY EFFICIENCY</h3>
    <p style="top:32px">With one of our audits to your business or home we can lower your energy bills and minimise your carbon footprint</p>
  </div>
  <div class="svc" style="top:670px;height:77px">
    <svg style="top:10px" width="30" height="58" viewBox="0 0 30 58"><path d="M22 2l6 4-4 3-10 25" stroke="#7dcf90" stroke-width="4" fill="none"/><path d="M8 32l12 6-6 18-12-4z" fill="#7dcf90"/></svg>
    <h3 style="top:6px">UNDERGROUND LOCATING</h3>
    <p style="top:34px">We have the tools and knowledge in locating underground utilities.</p>
  </div>
  <div class="pill g" style="left:774px;top:759px;width:126px">More Details<i></i></div>
</main>

<section class="abs band"></section>
<section>
  <article class="case" style="left:89px">
    <div class="ph" role="img" aria-label="Air conditioning outdoor unit installed against a wall"></div>
    <h4>CASE STUDY</h4>
    <p>Lorem ipsum dolor sit amet, co nsectetur adipiscing elit. Viv amus ante orci, tristique eu</p>
    <div class="more">Full details <b></b></div>
  </article>
  <article class="case" style="left:371px">
    <div class="ph" role="img" aria-label="Air conditioning outdoor unit installed against a wall"></div>
    <h4>CASE STUDY</h4>
    <p>Lorem ipsum dolor sit amet, co nsectetur adipiscing elit. Viv amus ante orci, tristique eu</p>
    <div class="more">Full details <b></b></div>
  </article>
  <article class="case" style="left:653px">
    <div class="ph" role="img" aria-label="Air conditioning outdoor unit installed against a wall"></div>
    <h4>CASE STUDY</h4>
    <p>Lorem ipsum dolor sit amet, co nsectetur adipiscing elit. Viv amus ante orci, tristique eu</p>
    <div class="more">Full details <b></b></div>
  </article>
</section>

<section>
  <h2 class="foot-h" style="left:92px;top:974px">Latest news</h2>
  <div class="news" style="top:1012px"><h5>Electricity prices to soar</h5><p>The Australian government's carbon tax will see electricity prices soar ... <a>more</a></p></div>
  <div class="abs" style="left:92px;top:1066px;width:203px;border-top:1px dashed #ccc"></div>
  <div class="news" style="top:1079px"><h5>Electricity prices to soar</h5><p>The Australian government's carbon tax will see electricity prices soar ... <a>more</a></p></div>
  <a class="abs green-link" style="left:93px;top:1134px;font-size:9.5px">View all news</a>
  <i class="vline" style="left:311px"></i>

  <h2 class="foot-h" style="left:330px;top:970px">Testimonials</h2>
  <div class="abs" style="left:325px;top:1002px;font-size:26px;font-weight:700;color:#999">&ldquo;</div>
  <p class="abs quote">&nbsp;&nbsp;&nbsp;&nbsp;&nbsp;Trelwire Fix is an electrical contractor based in Melbourne, Victoria. With experience in a lot of areas, there is pretty much nothing that Trelwire Fix won't take on. As well as electrical contracting we are trained in underground locating and energy efficiency.</p>
  <i class="vline" style="left:545px"></i>

  <h2 class="foot-h" style="left:570px;top:966px">We're here to help...</h2>
  <p class="abs form-intro">If you would like us to contact you to discuss your interests and/or requirements, please provide contact details:</p>
  <div class="field" style="top:1038px">Name*<span></span></div>
  <div class="field" style="top:1062px">Email*<span></span></div>
  <div class="field" style="top:1086px">Telephone<span></span></div>
  <div class="pill g" style="left:571px;top:1109px;width:129px">Submit<i></i></div>
  <div class="abs badge"></div>
  <div class="abs badge-bar"></div>
</section>

<footer class="abs footer"><p>Copyright © 2013 Trelwire Fix- All Rights Reserved</p></footer>

</body>
</html>
```